Customs House descriptive business cards

We require a two-sided business card that has a simple yet elegant design. We want to be able to promote our services as a customs house. This card should include our logo, contact info and services offered with the logo being on one side and the contact info and services on the flip side

Target Market(s)

Importers / exporters to and from the Bahamas

Industry/Entity Type

Logistics

Contact Information for Business Card

The front side of the card could have the logo and the flip side should have the other relevant info

Font styles to use
Serif

Colors

Designer to choose colors to be used in the design.

Requirements
Must have
• (Harbourline Agents Ltd) Logo, address and contact info also services:
• import customs clearance, Delivery & HAndling services,Florida pickups, Export packing & Crating Services, export customs clearance, Consulting

```html
<!DOCTYPE html>
<html lang="en">
<head>
<meta charset="utf-8">
<title>Harbourline Agents Ltd – Business Card</title>
<link href="https://fonts.googleapis.com/css2?family=Cinzel:wght@700&family=Lato:wght@400;700&display=swap" rel="stylesheet">
<style>
  :root {
    --bg: #e9ebee;
    --paper: #ffffff;
    --brand-blue: #1f88d2;
    --brand-blue-light: #2c9ee3;
    --brand-blue-deep: #1677c2;
    --ink: #1e1e1e;
    --rule: #c9cdd2;
  }
  * { box-sizing: border-box; margin: 0; padding: 0; }
  html, body { width: 1200px; height: 782px; overflow: hidden; background: var(--bg); }
  .canvas { position: relative; width: 1200px; height: 782px; }

  .card {
    position: absolute; top: 236px; width: 540px; height: 310px;
    box-shadow: 0 10px 26px rgba(0,0,0,.18); overflow: hidden;
  }

  /* Contact side */
  .card--contact { left: 45px; background: var(--paper); }
  .brand {
    position: absolute; left: 38px; top: 88px; width: 212px;
    display: flex; align-items: center; gap: 10px;
  }
  .brand__dot { width: 14px; height: 14px; border-radius: 50%; background: var(--brand-blue); flex: none; }
  .brand__name {
    font-family: 'Lato', sans-serif; font-weight: 700; font-size: 21px;
    line-height: 1.15; color: var(--brand-blue); letter-spacing: .5px;
  }
  .divider {
    position: absolute; left: 262px; top: 52px; width: 1px; height: 150px; background: var(--rule);
  }
  .contact { position: absolute; left: 290px; top: 58px; width: 236px; font-family: 'Lato', sans-serif; color: var(--ink); }
  .contact__name {
    font-family: 'Cinzel', serif; font-weight: 700; font-size: 17px;
    color: var(--brand-blue); letter-spacing: .5px;
  }
  .contact__role { font-size: 11px; letter-spacing: .6px; margin-bottom: 8px; text-transform: uppercase; }
  .contact__row {
    display: flex; align-items: center; gap: 7px;
    font-size: 12.5px; letter-spacing: .4px; text-transform: uppercase; line-height: 19px;
    white-space: nowrap;
  }
  .contact__row svg { width: 11px; height: 11px; fill: var(--brand-blue); flex: none; }
  .contact__address { font-size: 12.5px; letter-spacing: .4px; text-transform: uppercase; line-height: 17px; margin-top: 4px; }

  .services {
    position: absolute; left: 0; bottom: 0; width: 100%; height: 78px;
    background: linear-gradient(90deg, var(--brand-blue-deep), var(--brand-blue-light));
    color: #fff; font-family: 'Lato', sans-serif; font-size: 13px; letter-spacing: .2px;
    padding: 18px 22px 0; line-height: 21px; white-space: nowrap;
  }

  /* Brand side */
  .card--brand { left: 615px; }
  .card__pattern {
    position: absolute; inset: 0;
    background: radial-gradient(ellipse at 40% 40%, var(--brand-blue-light), var(--brand-blue-deep));
  }
  .card__mark {
    position: absolute; right: 40px; bottom: 46px;
    font-family: 'Lato', sans-serif; font-weight: 700; font-size: 16px; color: #fff; letter-spacing: .5px;
  }
</style>
</head>
<body>
<main class="canvas">

  <section class="card card--contact" aria-label="Contact side">
    <div class="brand">
      <span class="brand__dot"></span>
      <span class="brand__name">HARBOURLINE AGENTS LTD</span>
    </div>
    <div class="divider"></div>
    <div class="contact">
      <p class="contact__name">MARCUS DELANEY</p>
      <p class="contact__role">Managing Director</p>
      <p class="contact__row">
        <svg viewBox="0 0 24 24"><path d="M6.6 10.8a15.1 15.1 0 0 0 6.6 6.6l2.2-2.2c.3-.3.7-.4 1-.2 1.1.4 2.3.6 3.6.6.6 0 1 .4 1 1V20c0 .6-.4 1-1 1A17 17 0 0 1 3 4c0-.6.4-1 1-1h3.5c.6 0 1 .4 1 1 0 1.3.2 2.5.6 3.6.1.3 0 .7-.2 1z"/></svg>
        242-555 0187
      </p>
      <p class="contact__row">
        <svg viewBox="0 0 24 24"><path d="M2 5h20v14H2z"/></svg>
        info@harbourline.com
      </p>
      <p class="contact__row">
        <svg viewBox="0 0 24 24"><circle cx="12" cy="12" r="10"/></svg>
        www.harbourline.com
      </p>
      <p class="contact__address">18 Bay Street, Nassau<br>Bahamas, N-4821</p>
    </div>
    <div class="services">
      Import customs clearance | Delivery &amp; HAndling services | Florida pickups<br>
      Export packing &amp; Crating Services | Export customs clearance | Consulting
    </div>
  </section>

  <section class="card card--brand" aria-label="Brand side">
    <div class="card__pattern" role="img" aria-label="Blue background with a faint repeating brand pattern"></div>
    <span class="card__mark">Harbourline</span>
  </section>

</main>
</body>
</html>
```